Brell Harbor Company Business Cards

Front and Back Business Card - logo and text setup - cool design. I need workable photoshop or illustrator files so I can setup each employee card with design that is created
Updates

Hi everyone, thank you for the great entries. Please no more white and blue cards - there are so many already - black and silver only now please. thanks!

Target Market(s)

Construction Industry - Facility Managers

Industry/Entity Type

Construction

Contact Information for Business Card

I really like contemporary simplistic looks - clean neat....not opposed to seeing some black backrounds

Requirements
Must have
• Logo/website address with design on front only - www.brellharbor-example.com (logo attached)
• Back:
• Name/Title/Company Address/Phone/email address
Nice to have
• Cool design
Should not have
• Nothing gimmicky like Fire or Water - since we are a Fire Protection company - it has all been done

```html
<!DOCTYPE html>
<html lang="en">
<head>
<meta charset="utf-8">
<title>Brell Harbor Company Business Cards</title>
<link href="https://fonts.googleapis.com/css2?family=Source+Sans+3:wght@400;600;800&display=swap" rel="stylesheet">
<style>
  :root {
    --backdrop: #6e7784;
    --card-black: #1c1d20;
    --card-black-deep: #0c0c0e;
    --silver: #c9ccd1;
    --silver-light: #eef0f2;
    --silver-mid: #b4b8be;
    --silver-soft: #8d9198;
    --ink-black: #141517;
  }
  * { margin: 0; padding: 0; box-sizing: border-box; }
  html, body { width: 1200px; height: 1023px; overflow: hidden; }
  body {
    background: var(--backdrop);
    font-family: "Source Sans 3", sans-serif;
    display: flex; flex-direction: column; align-items: center; justify-content: center;
    gap: 40px;
  }
  .card {
    width: 800px; height: 457px; border-radius: 28px; position: relative; overflow: hidden;
    box-shadow: 0 10px 30px rgba(0,0,0,.3);
  }
  .card-back {
    background: linear-gradient(135deg, var(--card-black) 0%, var(--card-black-deep) 100%);
    color: var(--silver);
  }
  .holder { position: absolute; left: 70px; bottom: 80px; }
  .holder-name { font-size: 34px; font-weight: 600; line-height: 1.1; color: var(--silver-light); }
  .holder-title { font-size: 22px; font-weight: 400; }
  .divider {
    position: absolute; left: 400px; top: 70px; height: 317px; width: 4px;
    background: repeating-linear-gradient(to bottom, var(--silver-soft) 0 9px, transparent 9px 14px);
  }
  .contact { position: absolute; left: 440px; top: 80px; font-size: 22px; line-height: 1.35; }
  .address { margin-bottom: 36px; }
  .contact-row { display: flex; align-items: center; gap: 12px; }
  .contact-row svg { width: 20px; height: 20px; flex: none; }
  .card-front {
    background: linear-gradient(135deg, var(--silver-light) 0%, var(--silver) 55%, var(--silver-mid) 100%);
  }
  .brand {
    position: absolute; left: 0; right: 0; top: 160px; text-align: center;
    font-size: 76px; font-weight: 800; color: var(--ink-black); letter-spacing: -1px;
  }
  .front-url {
    position: absolute; left: 0; right: 0; top: 300px; text-align: center;
    font-size: 22px; color: var(--ink-black);
  }
</style>
</head>
<body>
  <section class="card card-back" aria-label="Card back">
    <div class="holder">
      <div class="holder-name">Dana Reyes</div>
      <div class="holder-title">Director</div>
    </div>
    <div class="divider"></div>
    <div class="contact">
      <div class="address">48 Harbor Loop<br>Port Calder, NY 10000</div>
      <div class="contact-row">
        <svg viewBox="0 0 20 20"><path fill="#c9ccd1" d="M5 2l3 4-2 2c1 2 3 4 5 5l2-2 4 3-2 3C9 17 3 11 2 5z"/></svg>
        <span>(555) 014-2280</span>
      </div>
      <div class="contact-row">
        <svg viewBox="0 0 20 20"><rect x="3" y="7" width="14" height="9" rx="1" fill="#c9ccd1"/><rect x="6" y="3" width="8" height="5" fill="none" stroke="#c9ccd1" stroke-width="1.6"/></svg>
        <span>(555) 014-2281</span>
      </div>
      <div class="contact-row">
        <svg viewBox="0 0 20 20"><rect x="2" y="5" width="16" height="11" rx="1" fill="#c9ccd1"/><path d="M2 5l8 6 8-6" fill="none" stroke="#1c1d20" stroke-width="1.5"/></svg>
        <span>info@brellharbor-example.com</span>
      </div>
      <div class="contact-row">
        <svg viewBox="0 0 20 20"><circle cx="10" cy="10" r="8" fill="#c9ccd1"/><path d="M2 10h16M10 2c-3 3-3 13 0 16M10 2c3 3 3 13 0 16" fill="none" stroke="#1c1d20" stroke-width="1.3"/></svg>
        <span>www.brellharbor-example.com</span>
      </div>
    </div>
  </section>

  <section class="card card-front" aria-label="Card front">
    <div class="brand">Brell Harbor</div>
    <div class="front-url">www.brellharbor-example.com</div>
  </section>
</body>
</html>
```